Business Card and Staionary Package for A Landscape Design Build Company
Silver Fern Yardworks Co, LLC.
Bright & Fun-filled
Neil P. Beckett, BLA, NHPA
Owner
(2) Locations P.O Box 4187 Gulfport, Mississippi 39506 P.O. Box 5903 Mobile, Alabama 36619
MS Office (228)-631-2947; AL Office (251)-749-3368
mbeckett@silverfernyardworks.example
silverfernyardworks.example
MS Contractor # 52819-SC; MS Landscape #LT214; AL Landscape # PSH-3561; NHPA Certififed Installer
Open to all design suggestion, please feel free to use your own ideas.

```html
<!DOCTYPE html>
<html lang="en">
<head>
<meta charset="utf-8">
<title>Silver Fern Yardworks Co — Stationery</title>
<link href="https://fonts.googleapis.com/css2?family=Lato:wght@400;700&display=swap" rel="stylesheet">
<style>
  :root{
    --green:#6cbf4b;
    --green-light:#8fd06f;
    --brown:#5b3f2b;
    --paper:#ffffff;
    --bg:#eef0ee;
    --ink:#6a6a6a;
  }
  *{box-sizing:border-box;margin:0;padding:0}
  html,body{width:1200px;height:936px;overflow:hidden;background:var(--bg);font-family:'Lato',sans-serif}
  .canvas{position:relative;width:1200px;height:936px}
  .piece{position:absolute;background:var(--paper);box-shadow:0 2px 6px rgba(0,0,0,.18);overflow:hidden}
  .piece svg.swoosh{position:absolute;left:0;top:0;width:100%}
  .brand{position:absolute;display:flex;align-items:center;gap:6px;color:var(--brown);font-weight:700;line-height:1.05;text-transform:uppercase;letter-spacing:.5px}
  .brand .dot{flex:none;border-radius:50%;background:var(--green)}
  .brand.on-green{color:#fff}
  .brand.on-green .dot{background:#fff}

  /* letterhead */
  .letterhead{left:38px;top:63px;width:533px;height:584px}
  .letterhead .brand{left:34px;top:84px;font-size:13px;width:170px}
  .letterhead .brand .dot{width:18px;height:18px}
  .letter-body{position:absolute;left:106px;top:158px;width:380px;font-size:6.2px;color:var(--ink);line-height:1.55}
  .letter-body p{margin-bottom:9px}
  .signature{width:40px;height:14px;background:#8a8a8a;border-radius:3px;margin:6px 0 4px}
  .letter-foot{position:absolute;left:34px;right:34px;bottom:22px;font-size:5.8px;color:var(--green);line-height:1.6;text-align:left}

  /* folder */
  .folder{left:634px;top:63px;width:533px;height:559px;background:var(--green)}
  .folder-band{position:absolute;left:0;right:0;top:220px;height:150px;background:#fff}
  .folder-band::before,.folder-band::after{content:"";position:absolute;left:0;right:0;height:10px;background:var(--green-light)}
  .folder-band::before{top:-10px}
  .folder-band::after{bottom:-10px}
  .folder .brand{left:50%;top:50%;transform:translate(-50%,-50%);font-size:24px;width:340px;justify-content:center;text-align:center}
  .folder .brand .dot{width:30px;height:30px}

  /* business cards */
  .card{left:38px;width:190px;height:89px}
  .card-front{top:672px}
  .card-front .brand{left:10px;top:44px;font-size:8px;width:120px}
  .card-front .brand .dot{width:10px;height:10px}
  .card-back{top:786px;background:var(--green)}
  .card-back .brand{left:12px;top:34px;font-size:9px;width:170px}
  .card-back .brand .dot{width:11px;height:11px}

  /* envelopes */
  .envelope-front{left:261px;top:672px;width:373px;height:203px}
  .envelope-front .brand{left:26px;top:80px;font-size:12px;width:170px}
  .envelope-front .brand .dot{width:14px;height:14px}
  .envelope-back{left:660px;top:672px;width:507px;height:203px}
  .envelope-back .seal{position:absolute;left:50%;top:44px;width:40px;height:40px;margin-left:-20px;border-radius:50%;background:#fff}
</style>
</head>
<body>
<div class="canvas">

  <section class="piece letterhead">
    <svg class="swoosh" viewBox="0 0 533 80" height="80" aria-hidden="true">
      <path d="M0 0H533V22C380 30 180 44 0 62Z" fill="var(--green)"/>
      <path d="M0 68C180 50 380 36 533 28" stroke="var(--brown)" stroke-width="4" fill="none"/>
    </svg>
    <div class="brand"><span class="dot"></span><span>Silver Fern Yardworks Co, LLC.</span></div>
    <div class="letter-body">
      <p>June 2, 2015</p>
      <p>Dear Client,<br>1000 Street Name, City, State</p>
      <p>Thank you for considering our team for your landscape project. We design and build outdoor spaces that bring lasting beauty to your home, with careful planning, quality plants and skilled installation from start to finish.</p>
      <p>Our crews handle grading, planting, hardscape and irrigation, and every job is reviewed on site so the result matches the plan we agreed on together.</p>
      <p>We would be glad to visit your property, talk through ideas and prepare a clear estimate. Please call either office or send us an email at any time.</p>
      <p>Warm Regards,</p>
      <div class="signature" role="img" aria-label="Handwritten signature"></div>
      <p>Neil P. Beckett, BLA, NHPA<br>Owner</p>
    </div>
    <div class="letter-foot">
      P.O Box 4187 Gulfport, Mississippi 39506 · MS Office (228)-631-2947 · P.O. Box 5903 Mobile, Alabama 36619 · AL Office (251)-749-3368<br>
      mbeckett@silverfernyardworks.example · silverfernyardworks.example · MS Contractor # 52819-SC · MS Landscape #LT214 · AL Landscape # PSH-3561 · NHPA Certified Installer
    </div>
  </section>

  <section class="piece folder">
    <div class="folder-band">
      <div class="brand"><span class="dot"></span><span>Silver Fern Yardworks Co, LLC.</span></div>
    </div>
  </section>

  <section class="piece card card-front">
    <svg class="swoosh" viewBox="0 0 190 40" height="40" aria-hidden="true">
      <path d="M0 0H190V8C130 12 60 20 0 30Z" fill="var(--green)"/>
      <path d="M0 33C60 23 130 15 190 11" stroke="var(--brown)" stroke-width="2" fill="none"/>
    </svg>
    <div class="brand"><span class="dot"></span><span>Silver Fern Yardworks Co</span></div>
  </section>

  <section class="piece card card-back">
    <div class="brand on-green"><span class="dot"></span><span>Silver Fern Yardworks Co</span></div>
  </section>

  <section class="piece envelope-front">
    <svg class="swoosh" viewBox="0 0 373 70" height="70" aria-hidden="true">
      <path d="M0 0H373V18C260 26 120 40 0 56Z" fill="var(--green)"/>
      <path d="M0 61C120 45 260 31 373 24" stroke="var(--brown)" stroke-width="3" fill="none"/>
    </svg>
    <div class="brand"><span class="dot"></span><span>Silver Fern Yardworks Co, LLC.</span></div>
  </section>

  <section class="piece envelope-back">
    <svg class="swoosh" viewBox="0 0 507 100" height="100" aria-hidden="true">
      <rect width="507" height="100" fill="var(--green)"/>
    </svg>
    <span class="seal"></span>
  </section>

</div>
</body>
</html>
```